Simple templates for management consulting firm

Vireo Advisors is a management consulting firm based in the DC area. We have all the basic templates but would like to tweak them so they look consistent.

Check us out at www.vireoadvisors-example.com

For this project we would like to get
a tweaked powerpoint template (header should be up)
a letter template for letters
a fax template

Current templates and our logo are attached.
Updates

We just increased the budget of this project.

We got questions about the project. Here are our thoughts on this one:

Please include the logo into the fax template. If you find improvements in the layout then feel free to make those. Let's not overthink this too much. Keep it simple :)

We like The powerpoint concept as is. The slide titles are for some reasons on the bottom. It seems to irritate some folks. If you can switch the slide titles to the top, keep the look and feel of the slides and work in the logo then that would be fantastic.

The letter head should include the following

Vireo Advisors, LLC Box 5817, Pine Hollow, VA 20499 Phone 555 814-2906, Fax 555 276 9143, www.vireoadvisors-example.com and the logo.

Again, let's keep it simple.

Thank you for considering this project.

We just realize that we are not necessarily inisting to use the red in the slides.
Any approach that would work with the logo will be considered.

Thanks for your creativity.

Target Market(s)

tech companies, Meridian 400, venture capitalists

Industry/Entity Type

Management Consulting

Requirements
Must have
• Keep it simple please

```html
<!DOCTYPE html>
<html lang="en">
<head>
<meta charset="utf-8">
<title>Vireo Advisors – PowerPoint Template</title>
<link rel="stylesheet" href="https://fonts.googleapis.com/css2?family=Play:wght@400;700&display=swap">
<style>
  :root {
    --canvas: #ffffff;
    --label: #8a8a8a;
    --gold: #c9a02e;
    --logo-grey: #8d8d8d;
    --name: #3a0c10;
    --slide-light: #ffffff;
    --slide-dark: #a9a9a9;
    --band: #f4f4f4;
    --band-line: #dcdcdc;
    --footer-text: #8a8a8a;
  }
  * { box-sizing: border-box; margin: 0; padding: 0; }
  html, body {
    width: 1200px; height: 960px; overflow: hidden;
    background: var(--canvas);
    font-family: "Play", sans-serif;
  }
  .board { position: relative; width: 1200px; height: 960px; }

  .label {
    position: absolute; font-size: 15px; line-height: 19px; color: var(--label);
  }
  .label--right { text-align: right; }

  .slide {
    position: absolute; overflow: hidden;
    box-shadow: 2px 3px 6px rgba(0,0,0,0.35);
  }

  /* Brand lockup: plain circle + name in one colour and weight */
  .brand { position: absolute; display: flex; align-items: center; }
  .brand__dot { border-radius: 50%; background: var(--gold); flex: none; }
  .brand__name {
    color: var(--logo-grey); font-weight: 400; letter-spacing: 0.04em;
    text-transform: uppercase; white-space: nowrap;
  }

  /* Zoomed first slide */
  .zoom-first {
    left: 14px; top: 86px; width: 541px; height: 320px;
    background: radial-gradient(ellipse at 40% 45%, #ffffff 0%, #f4f4f4 55%, #e4e4e4 100%);
  }
  .zoom-first .brand { left: 100px; top: 134px; }
  .zoom-first .brand__dot { width: 60px; height: 60px; margin-right: 12px; }
  .zoom-first .brand__name { font-size: 30px; }

  /* Full first slide */
  .first-slide {
    left: 585px; top: 17px; width: 595px; height: 458px;
    background: radial-gradient(ellipse 60% 62% at 50% 48%, var(--slide-light) 0%, #f2f2f2 40%, #cfcfcf 78%, var(--slide-dark) 100%);
  }
  .first-slide .brand { left: 190px; top: 209px; }
  .first-slide .brand__dot { width: 42px; height: 42px; margin-right: 9px; }
  .first-slide .brand__name { font-size: 18px; }

  /* Zoomed top band */
  .zoom-top {
    left: 14px; top: 489px; width: 541px; height: 204px;
    background: linear-gradient(#eeeeee, #dedede);
  }
  .zoom-top__band {
    position: absolute; left: 0; top: 0; width: 100%; height: 104px;
    background: linear-gradient(#ffffff, var(--band));
    border-bottom: 1px solid var(--band-line);
  }
  .zoom-top .brand { left: 48px; top: 28px; }
  .zoom-top .brand__dot { width: 50px; height: 50px; margin-right: 12px; }
  .zoom-top .brand__name { font-size: 36px; }

  /* Second slide */
  .second-slide {
    left: 585px; top: 489px; width: 595px; height: 462px;
    background: radial-gradient(ellipse 70% 60% at 48% 40%, #ffffff 0%, #f1f1f1 45%, #d6d6d6 100%);
  }
  .second-slide__header {
    position: absolute; left: 0; top: 0; width: 100%; height: 46px;
    background: linear-gradient(#ffffff, var(--band));
    border-bottom: 1px solid var(--band-line);
  }
  .second-slide .brand { left: 22px; top: 13px; }
  .second-slide .brand__dot { width: 21px; height: 21px; margin-right: 5px; }
  .second-slide .brand__name { font-size: 17px; }
  .presenter { position: absolute; left: 21px; top: 203px; color: var(--name); }
  .presenter__name { font-size: 25px; font-weight: 700; line-height: 30px; }
  .presenter__role { font-size: 17px; line-height: 21px; }
  .second-slide__footer {
    position: absolute; left: 0; bottom: 0; width: 100%; height: 20px;
    background: var(--band); border-top: 1px solid var(--band-line);
    font-size: 9px; line-height: 19px; color: var(--footer-text);
    text-align: right; padding-right: 14px;
  }
</style>
</head>
<body>
<main class="board">
  <p class="label label--right" style="left:400px; top:14px; width:153px;">powerpoint template<br>first slide</p>
  <p class="label" style="left:20px; top:63px;">Zoom first slide</p>

  <section class="slide zoom-first">
    <div class="brand"><span class="brand__dot"></span><span class="brand__name">Vireo Advisors</span></div>
  </section>

  <section class="slide first-slide">
    <div class="brand"><span class="brand__dot"></span><span class="brand__name">Vireo Advisors</span></div>
  </section>

  <p class="label" style="left:20px; top:463px;">Zoom top slide</p>

  <section class="slide zoom-top">
    <div class="zoom-top__band"></div>
    <div class="brand"><span class="brand__dot"></span><span class="brand__name">Vireo Advisors</span></div>
  </section>

  <p class="label label--right" style="left:380px; top:704px; width:173px;">powerpoint template<br>second slide</p>

  <section class="slide second-slide">
    <div class="second-slide__header"></div>
    <div class="brand"><span class="brand__dot"></span><span class="brand__name">Vireo Advisors</span></div>
    <div class="presenter">
      <p class="presenter__name">Alan Brooke</p>
      <p class="presenter__role">Managing Partner</p>
    </div>
    <footer class="second-slide__footer">Copyright © 2012 | Vireo Advisors</footer>
  </section>
</main>
</body>
</html>
```